Shisha Hookah Charcoal Box Packing Design + Logo

Im looking for someone to create a packaging for our cubed shisha charcoal product mainly targeted at the shisha smoking market in the middle east and around the Globe.

I want to see 2 Colour schemes: Black/Gold Black/Copper

Brand Name: "Velvet Ember" and must have the "C" like in the picture attached.

The overall feel of the packaging should be luxury yet fresh and funky with the highest of quality again see the picture attached.

Packaging: Flat / Rectangular

Target Market(s)

Shisha Hookah Smokers in the Middle East and over the globe

Industry/Entity Type

Product

Font styles to use
Script

Requirements
Must have
• The Words "Velvet Ember" and the "C" on the box.

```html
<!DOCTYPE html>
<html lang="en">
<head>
<meta charset="utf-8">
<title>Velvet Ember – Premium Shisha Charcoal box dieline</title>
<link href="https://fonts.googleapis.com/css2?family=Pinyon+Script&family=Cormorant+Garamond:ital,wght@1,400&family=Arimo:wght@400&display=swap" rel="stylesheet">
<style>
  :root {
    --paper: #ffffff;
    --board: #080a09;
    --gold: #cba254;
    --copper: #b5541e;
    --fold-line: #e8e8e8;
    --slot: #5a4a2a;
  }
  html, body {
    margin: 0;
    padding: 0;
    width: 1200px;
    height: 1200px;
    overflow: hidden;
    background: var(--paper);
  }
  .dieline {
    position: relative;
    width: 1200px;
    height: 1200px;
  }
  .dieline__shapes {
    position: absolute;
    inset: 0;
  }
  .print {
    position: absolute;
    color: var(--gold);
    white-space: nowrap;
  }
  .upside-down { transform: translate(-50%, -50%) rotate(180deg); }
  .centered { transform: translate(-50%, -50%); }

  .wordmark {
    font-family: "Pinyon Script", cursive;
    font-weight: 400;
    line-height: 1;
  }
  .wordmark--hero { font-size: 92px; }
  .wordmark--band { font-size: 58px; }
  .wordmark--lid { font-size: 44px; }
  .wordmark--seal { font-size: 38px; }
  .wordmark--seal-small { font-size: 24px; }

  .tagline {
    font-family: "Arimo", Arial, sans-serif;
    font-size: 15px;
    letter-spacing: 0.2px;
  }
  .tagline--small { font-size: 12px; }

  .weight-mark {
    font-family: "Pinyon Script", cursive;
    font-size: 36px;
  }

  .info-panel {
    position: absolute;
    left: 398px;
    top: 210px;
    width: 402px;
    height: 156px;
    box-sizing: border-box;
    border: 1px solid var(--gold);
    padding: 12px 14px;
    transform: rotate(180deg);
    color: var(--gold);
    font-family: "Cormorant Garamond", Georgia, serif;
    font-style: italic;
    font-size: 11.5px;
    line-height: 14px;
    text-align: justify;
  }
</style>
</head>
<body>
<main class="dieline">
  <svg class="dieline__shapes" width="1200" height="1200" viewBox="0 0 1200 1200">
    <defs>
      <path id="window-edge"
        d="M376 0 Q372 14 352 26 Q340 36 346 50 Q352 60 350 66 Q340 78 346 92 Q352 104 344 118 Q338 140 346 156 Q352 170 344 186 Q342 206 356 222 Q366 240 362 260 Q352 290 364 316" />
    </defs>

    <!-- top lid flap -->
    <polygon class="lid" fill="var(--board)"
      points="138,52 1062,52 1062,171 932,181 268,181 138,171" />
    <line x1="268" y1="52" x2="268" y2="181" stroke="var(--fold-line)" stroke-width="1"/>
    <line x1="932" y1="52" x2="932" y2="181" stroke="var(--fold-line)" stroke-width="1"/>

    <!-- upper side walls -->
    <rect class="side-wall" x="6" y="181" width="1188" height="316" fill="var(--gold)"/>
    <line x1="138" y1="181" x2="138" y2="497" stroke="var(--slot)" stroke-width="1.2"/>
    <line x1="1062" y1="181" x2="1062" y2="497" stroke="var(--slot)" stroke-width="1.2"/>
    <rect x="263" y="240" width="4" height="33" fill="none" stroke="var(--slot)" stroke-width="1"/>
    <rect x="263" y="390" width="4" height="34" fill="none" stroke="var(--slot)" stroke-width="1"/>
    <rect x="932" y="240" width="4" height="33" fill="none" stroke="var(--slot)" stroke-width="1"/>
    <rect x="932" y="390" width="4" height="34" fill="none" stroke="var(--slot)" stroke-width="1"/>
    <rect x="3" y="240" width="4" height="33" fill="var(--copper)"/>
    <rect x="3" y="390" width="4" height="34" fill="var(--copper)"/>
    <rect x="1193" y="240" width="4" height="33" fill="var(--copper)"/>
    <rect x="1193" y="390" width="4" height="34" fill="var(--copper)"/>

    <!-- upper black panel -->
    <g class="panel" transform="translate(0,181)">
      <path fill="var(--board)"
        d="M376 0 L824 0 Q828 14 848 26 Q860 36 854 50 Q848 60 850 66 Q860 78 854 92 Q848 104 856 118 Q862 140 854 156 Q848 170 856 186 Q858 206 844 222 Q834 240 838 260 Q848 290 836 316 L364 316 Q352 290 362 260 Q366 240 356 222 Q342 206 344 186 Q352 170 346 156 Q338 140 344 118 Q352 104 346 92 Q340 78 350 66 Q352 60 346 50 Q340 36 352 26 Q372 14 376 0 Z"/>
    </g>

    <!-- middle band (front wall) -->
    <polygon class="front-wall" fill="var(--board)"
      points="138,505 268,497 932,497 1062,505 1062,617 932,628 268,628 138,617" />

    <!-- lower side walls -->
    <polygon class="side-wall" fill="var(--gold)"
      points="138,651 376,628 824,628 1062,651 1062,920 824,943 376,943 138,920" />

    <!-- lower black panel (base) -->
    <g class="panel" transform="translate(0,943) scale(1,-1)">
      <path fill="var(--board)"
        d="M364 0 L836 0 Q848 26 838 56 Q834 76 844 94 Q858 110 856 130 Q848 146 854 160 Q862 176 856 198 Q848 212 854 224 Q860 238 850 250 Q848 256 854 266 Q860 280 848 290 Q828 302 824 316 L376 316 Q372 302 352 290 Q340 280 346 266 Q352 256 350 250 Q340 238 346 224 Q352 212 344 198 Q338 176 346 160 Q352 146 344 130 Q342 110 356 94 Q366 76 362 56 Q352 26 364 0 Z"/>
    </g>

    <!-- tuck tab -->
    <path class="tuck-tab" fill="var(--board)"
      d="M232 944 L968 944 Q1050 946 1051 990 Q1048 1040 932 1074 L268 1074 Q152 1040 149 990 Q150 946 232 944 Z"/>

    <!-- hookah illustration area -->
    <rect x="782" y="510" width="84" height="108" rx="4" fill="var(--gold)" opacity="0.85"
      role="img" aria-label="Gold line illustration of a hookah pipe with hose"/>
  </svg>

  <!-- lid -->
  <div class="print wordmark wordmark--seal centered" style="left:600px; top:124px;">Velvet Ember</div>

  <!-- upper panel (upside down) -->
  <div class="info-panel">Each cube is pressed from pure coconut shell and dried slowly for a clean, even glow. Light the cube on a coil until it is grey on every side, then set it on the foil or heat tray of your bowl. It gives a long, steady heat with little ash and no smell, so the flavour of your tobacco stays true from the first draw to the last. Keep the box dry and away from children. Never light indoors without fresh air. Made for shisha lovers across the Gulf, Europe and beyond, who ask for more from every session.</div>
  <div class="print tagline tagline--small upside-down" style="left:520px; top:405px;">Premium Shisha Charcoal</div>
  <div class="print wordmark wordmark--lid upside-down" style="left:530px; top:448px;">Velvet Ember</div>
  <div class="print wordmark wordmark--seal-small upside-down" style="left:718px; top:446px;">Velvet Ember</div>

  <!-- front wall (upside down) -->
  <div class="print tagline tagline--small upside-down" style="left:600px; top:526px;">Premium Shisha Charcoal</div>
  <div class="print wordmark wordmark--band upside-down" style="left:600px; top:568px;">Velvet Ember</div>

  <!-- base -->
  <div class="print wordmark wordmark--hero centered" style="left:600px; top:708px;">Velvet Ember</div>
  <div class="print tagline centered" style="left:598px; top:773px;">Premium Shisha Charcoal</div>
  <div class="print wordmark wordmark--seal centered" style="left:600px; top:876px;">Velvet Ember</div>

  <!-- tuck tab -->
  <div class="print wordmark wordmark--seal centered" style="left:600px; top:1010px;">Velvet Ember</div>
  <div class="print weight-mark centered" style="left:852px; top:1008px;">1 Kg</div>
</main>
</body>
</html>
```